Criação de Papelaria (6 itens) para Logística, Entrega & Armazenamento
A empresa queria:
" Trabalhamos no seguinte de logística, no qual engloba diversos seguimentos, como armazenagem, transporte , manuseio e entregas. Nosso foco é o atendimento personalizado ao cliente, suprindo toda a demanda e necessidade do cliente sem ocasionar nenhum transtorno ao mesmo. "

```html
<!DOCTYPE html>
<html lang="pt-BR">
<head>
<meta charset="UTF-8">
<title>Transvia – Papelaria</title>
<link href="https://fonts.googleapis.com/css2?family=Exo+2:wght@400;600;800&display=swap" rel="stylesheet">
<style>
  :root {
    --brand-red: #b51d27;
    --brand-red-dark: #9e1620;
    --paper: #ffffff;
    --ink-gray: #6b6b6b;
    --stage: #e9e9e9;
  }
  * { margin: 0; padding: 0; box-sizing: border-box; }
  html, body { width: 1200px; height: 1200px; overflow: hidden; }
  body {
    background: var(--stage);
    font-family: "Exo 2", sans-serif;
    position: relative;
  }

  /* Folder */
  .folder {
    position: absolute;
    left: 60px; top: 150px;
    width: 520px; height: 900px;
    background: var(--brand-red);
    overflow: hidden;
    box-shadow: 0 6px 20px rgba(0,0,0,.18);
  }
  .folder .wordmark {
    position: absolute;
    left: 48px; top: 56px;
    color: var(--paper);
  }
  .folder .decor-shape {
    position: absolute;
    left: 250px; top: 470px;
    width: 330px; height: 330px;
    border-radius: 60px;
    background: var(--brand-red-dark);
  }

  /* Wordmark */
  .wordmark .name {
    display: block;
    font-weight: 800;
    font-size: 40px;
    letter-spacing: 2px;
    line-height: 1;
  }
  .wordmark .tagline {
    display: block;
    font-weight: 400;
    font-size: 11px;
    letter-spacing: 5.2px;
    margin-top: 4px;
  }

  /* Envelope */
  .envelope {
    position: absolute;
    left: 620px; top: 150px;
    width: 520px; height: 900px;
    background: var(--paper);
    overflow: hidden;
    box-shadow: 0 6px 20px rgba(0,0,0,.18);
  }
  .envelope .flap {
    position: absolute;
    left: 0; top: 0;
    width: 520px; height: 130px;
  }
  .envelope .wordmark {
    position: absolute;
    left: 80px; top: 250px;
  }
  .envelope .wordmark .name {
    color: var(--brand-red);
    font-size: 52px;
    letter-spacing: 3px;
  }
  .envelope .wordmark .tagline {
    color: var(--ink-gray);
    font-size: 14px;
    letter-spacing: 7px;
  }
  .envelope .rule {
    position: absolute;
    left: 30px; right: 30px; top: 812px;
    height: 2px;
    background: var(--brand-red);
  }
  .envelope .contacts {
    position: absolute;
    left: 30px; right: 30px; top: 822px;
    display: flex;
    justify-content: space-between;
    font-size: 9px;
    color: var(--ink-gray);
    line-height: 15px;
  }
  .contacts .item { display: flex; align-items: center; gap: 5px; }
  .contacts .group { display: flex; flex-direction: column; }
  .contacts svg { width: 9px; height: 9px; fill: var(--brand-red); flex: none; }
  .envelope .base-band {
    position: absolute;
    left: 0; right: 0; bottom: 0;
    height: 22px;
    background: var(--brand-red);
  }
</style>
</head>
<body>

  <section class="folder">
    <div class="wordmark">
      <span class="name">TRANSVIA</span>
      <span class="tagline">SOLUÇÕES LOGÍSTICAS</span>
    </div>
    <div class="decor-shape"></div>
  </section>

  <section class="envelope">
    <svg class="flap" viewBox="0 0 520 130" preserveAspectRatio="none">
      <polygon points="0,0 520,0 520,60 470,130 50,130 0,60" fill="#b51d27"/>
    </svg>

    <div class="wordmark">
      <span class="name">TRANSVIA</span>
      <span class="tagline">SOLUÇÕES LOGÍSTICAS</span>
    </div>

    <div class="rule"></div>
    <div class="contacts">
      <div class="group">
        <span class="item">(11) 4000-2100
          <svg viewBox="0 0 10 10"><path d="M2 0.5 L4 2.5 L3 3.6 Q4.2 5.8 6.4 7 L7.5 6 L9.5 8 L8 9.5 Q2 9 0.5 2 Z"/></svg></span>
        <span class="item">(11) 4000-2101
          <svg viewBox="0 0 10 10"><path d="M2 0.5 L4 2.5 L3 3.6 Q4.2 5.8 6.4 7 L7.5 6 L9.5 8 L8 9.5 Q2 9 0.5 2 Z"/></svg></span>
      </div>
      <div class="group">
        <span class="item">contato@transvia.com.br
          <svg viewBox="0 0 10 10"><path d="M0.5 2 H9.5 V8 H0.5 Z M1 2.4 L5 5.5 L9 2.4" fill="none" stroke="#b51d27" stroke-width="1"/></svg></span>
        <span class="item">www.transvia.com.br
          <svg viewBox="0 0 10 10"><circle cx="5" cy="5" r="4.2" fill="none" stroke="#b51d27" stroke-width="1"/><path d="M1 5 H9 M5 1 Q2.5 5 5 9 Q7.5 5 5 1" fill="none" stroke="#b51d27" stroke-width="0.8"/></svg></span>
      </div>
      <div class="group">
        <span class="item">Rua das Docas, 120 - Centro
          <svg viewBox="0 0 10 10"><path d="M5 0.5 A3.3 3.3 0 0 1 8.3 3.8 Q8.3 6 5 9.5 Q1.7 6 1.7 3.8 A3.3 3.3 0 0 1 5 0.5 Z M5 2.6 A1.2 1.2 0 1 0 5 5 A1.2 1.2 0 1 0 5 2.6 Z" fill-rule="evenodd"/></svg></span>
        <span class="item">São Paulo/SP CEP 01000-000</span>
      </div>
    </div>
    <div class="base-band"></div>
  </section>

</body>
</html>
```